Need wine label for brand that is named: Casmerel Vineyards & Winery

Casmerel is a yoga way of breathing. In Sanskrit Casmerel means "flying up." I would like a creative wine label that articulates Casmerel. The label should include a graphic and the name Casmerel on one line and Vineyards & Winery in smaller print underneath Casmerel.

```html
<!DOCTYPE html>
<html lang="en">
<head>
<meta charset="utf-8">
<title>Casmerel Vineyards &amp; Winery — Wine Label</title>
<link rel="stylesheet" href="https://fonts.googleapis.com/css2?family=Cinzel:wght@400;500&display=swap">
<style>
  :root {
    --paper: #f3f3f1;
    --paper-shade: #e6e7e5;
    --ink: #4d6873;
    --ink-soft: #7f959d;
    --band: #9fb0b6;
  }
  html, body {
    margin: 0;
    padding: 0;
    width: 901px;
    height: 1200px;
    overflow: hidden;
    background: var(--paper);
  }
  .label {
    position: relative;
    width: 901px;
    height: 1200px;
    background: linear-gradient(100deg, var(--paper-shade) 0%, var(--paper) 22%, #fafaf9 50%, var(--paper) 78%, var(--paper-shade) 100%);
    font-family: "Cinzel", "Times New Roman", serif;
    color: var(--ink);
  }
  .border-band {
    position: absolute;
    left: 0;
    width: 901px;
    height: 62px;
    background: var(--band);
  }
  .border-band::before,
  .border-band::after {
    content: "";
    position: absolute;
    left: 0;
    right: 0;
    height: 4px;
    background: var(--ink);
  }
  .border-band::before { top: -12px; }
  .border-band::after { bottom: -12px; }
  .border-band--top { top: 78px; }
  .border-band--bottom { bottom: 78px; }

  .emblem {
    position: absolute;
    top: 230px;
    left: 50%;
    width: 380px;
    height: 380px;
    margin-left: -190px;
    border-radius: 50%;
    background: radial-gradient(circle, #b9c6ca 0%, var(--ink-soft) 70%, var(--ink) 100%);
  }

  .brand {
    position: absolute;
    top: 680px;
    left: 0;
    width: 901px;
    text-align: center;
  }
  .brand__name {
    margin: 0;
    font-size: 124px;
    font-weight: 400;
    line-height: 1;
    letter-spacing: 2px;
  }
  .brand__rule {
    width: 740px;
    height: 0;
    margin: 26px auto 0;
    border-top: 3px solid var(--ink-soft);
    border-bottom: 1px solid var(--ink-soft);
    padding-top: 5px;
  }
  .brand__tagline {
    margin: 28px 0 0;
    font-size: 54px;
    font-weight: 400;
    line-height: 1;
    letter-spacing: 1px;
  }
</style>
</head>
<body>
  <main class="label">
    <div class="border-band border-band--top" role="img" aria-label="Braided knot ornamental border"></div>

    <div class="emblem" role="img" aria-label="Circular mandala-style emblem"></div>

    <section class="brand">
      <h1 class="brand__name">CASMEREL</h1>
      <div class="brand__rule"></div>
      <p class="brand__tagline">VINEYARDS &amp; WINERY</p>
    </section>

    <div class="border-band border-band--bottom" role="img" aria-label="Braided knot ornamental border"></div>
  </main>
</body>
</html>
```